Print Ad for 2022 Prime Counsel Journal - Seeking a Creative Ad for a Creative Law Firm

We need an advertisement for the Prime Counsel annual publication, which will also be included in the Brookvale Gazette, a widely-read, stylish city magazine.

We would like our advertisement to be clever, stylish, and unique. We hate looking like other law firms and want an ad that is original, unexpected, clever, or stylish. We DO NOT want something traditional, boring, or typical for law firms - we separate ourselves in our market by NOT acting like a traditional law firm.

Marwick Tolland and Pryce, LLC provides full-service legal representation to entrepreneurs, individuals, and companies for all of their business, employment and litigation needs.
We have included THREE different photo options in the attachments. Please use ONLY ONE in the ad.

BE SURE TO REVIEW THE ATTACHMENTS. WE HAVE INCLUDED OUR ADS FOR PRIOR YEARS, BUT WE WANT A TOTALLY DIFFERENT LOOK THIS YEAR!! PLEASE DO NOT PROVIDE SIMILAR ADS.

For more information, please visit our website: www.mtplawgroup.example

Target Market(s)

Small business owners, individuals with employment law issues, entrepreneurs, other attorneys.

Industry/Entity Type

Legal

Font styles to use
Serif
Decorative

Colors

Designer to choose colors to be used in the design.

Requirements
Must have
• It must use our logo, our photo, and our tag line "The Name is Hard to Remember. The Results are Hard to Forget." 1. Use our full firm name of Jeselskis Brinkerhoff and Joseph, LLC2. Use our logo, attached AND our slogan - "THE NAME IS HARD TO REMEMBER. THE RESULTS ARE HARD TO FORGET." Please review the PDF attachments on the ad specs. The ad must follow the following requirements:• COLOR: Must be provided as CMYK, please convert if necessary. • IMAGES: All images must be precisely 300 dpi, placed at 100% to ensure print quality.• LOGOS: Preferred vector (.eps) format, (acceptable as high-res 300 dpi image).• TEXT: Should be editable within the ad. • PRIME COUNSEL REFERENCES: Please adhere to the attached advertising guidelines regarding the appropriate use of the Prime Counsel name, ad concepts and imagery.
Nice to have
• Highly stylized, memorable, upscale look. We really want to show our personality. We take our work seriously, but we don't take ourselves too seriously. Here are some other ads we like: https://issues.primecounsel.example/archive/ed1/page26 https://issues.primecounsel.example/archive/ed2/page4 https://www.searchlink.example/redirect?target=https%3A%2F%2Fwww.hollisvane.example%2Fhv-firm-honored-by-coastal-bar-review https://issues.primecounsel.example/archive/ed3/page4 https://issues.primecounsel.example/archive/ed4/page68
Should not have
• Scales of justice, traditional law firm style, or other design features that are predictable in law firm advertising. We don't like clutter or narrative copy.

```html
<!DOCTYPE html>
<html lang="en">
<head>
<meta charset="utf-8">
<title>Marwick Tolland and Pryce — Print Ad</title>
<link rel="stylesheet" href="https://fonts.googleapis.com/css2?family=Montserrat:wght@500;600;700&family=Caveat:wght@500;700&display=swap">
<style>
:root{
  --bg-light:#eeeeef;
  --bg-mid:#d9d9db;
  --bg-dark:#c4c4c7;
  --blue:#2a7fc4;
  --navy:#15213a;
  --ink:#1f2430;
  --paper:#fbfbfa;
  --twine:#6b5a48;
  --wood:#b88a5a;
  --wood-dark:#8e653d;
  --photo-a:#7a6a58;
  --photo-b:#a49684;
}
*{margin:0;padding:0;box-sizing:border-box}
html,body{width:885px;height:1200px;overflow:hidden}
body{font-family:"Montserrat",sans-serif;color:var(--ink)}
.ad{
  position:relative;width:885px;height:1200px;overflow:hidden;
  background:
    linear-gradient(115deg,transparent 38%,rgba(255,255,255,.55) 46%,transparent 55%),
    linear-gradient(115deg,transparent 58%,rgba(255,255,255,.4) 64%,transparent 70%),
    radial-gradient(ellipse at 55% 30%,var(--bg-light) 0%,var(--bg-mid) 60%,var(--bg-dark) 100%);
}
.firm-mark{
  position:absolute;top:70px;right:34px;display:flex;align-items:center;gap:10px;
}
.firm-mark__dot{width:26px;height:26px;border-radius:50%;background:var(--navy)}
.firm-mark__name{font-weight:700;font-size:22px;color:var(--navy);letter-spacing:1px}
.clothesline{position:absolute;left:0;top:230px}
.portrait{
  position:absolute;width:205px;padding:12px 12px 0;background:var(--paper);
  box-shadow:0 6px 14px rgba(0,0,0,.22);
}
.portrait__photo{width:181px;height:190px;background:linear-gradient(160deg,var(--photo-b),var(--photo-a))}
.portrait__caption{height:82px;padding:8px 2px 0;font-family:"Caveat",cursive;color:#333}
.portrait__name{font-size:19px;font-weight:700;line-height:1.05}
.portrait__note{font-size:12px;line-height:1.15}
.pin{position:absolute;width:18px;height:62px;border-radius:3px;
  background:linear-gradient(90deg,var(--wood-dark),var(--wood) 40%,var(--wood-dark))}
.tagline{position:absolute;top:738px;left:0;width:100%;text-align:center}
.tagline__lead{font-weight:700;font-size:33px;color:var(--blue)}
.tagline__close{font-weight:700;font-size:33px;color:var(--navy);margin-top:4px}
.practice{position:absolute;top:905px;left:0;width:100%;text-align:center}
.practice__title{font-weight:600;font-size:28px;color:var(--blue);margin-bottom:10px}
.practice__list{list-style:none;font-weight:500;font-size:22px;color:var(--navy);line-height:1.3}
.contact{position:absolute;left:44px;top:1098px;font-weight:600;font-size:20px;color:var(--navy)}
.contact__row{display:flex;align-items:center;gap:14px;margin-bottom:14px}
.contact__icon{width:26px;height:26px}
.social{position:absolute;right:36px;top:1140px;display:flex;gap:6px}
.social__slot{width:26px;height:26px;border-radius:5px;background:var(--navy)}
</style>
</head>
<body>
<main class="ad">
  <div class="firm-mark">
    <span class="firm-mark__dot"></span>
    <span class="firm-mark__name">MTP Legal</span>
  </div>

  <svg class="clothesline" width="885" height="140" viewBox="0 0 885 140">
    <path d="M0 30 Q440 130 885 40" fill="none" stroke="var(--twine)" stroke-width="3"/>
  </svg>

  <article class="portrait" style="left:18px;top:300px;transform:rotate(-3deg)">
    <div class="portrait__photo" role="img" aria-label="Portrait photo of attorney Grant Ellery"></div>
    <div class="portrait__caption">
      <div class="portrait__name">Grant Ellery</div>
      <div class="portrait__note">Selected to Prime Counsel 2018 - 2022</div>
      <div class="portrait__note">Selected to Rising Counsel 2014 - 2017</div>
    </div>
  </article>
  <article class="portrait" style="left:236px;top:330px;transform:rotate(2deg)">
    <div class="portrait__photo" role="img" aria-label="Portrait photo of attorney Sienna Marlowe"></div>
    <div class="portrait__caption">
      <div class="portrait__name">Sienna Marlowe</div>
      <div class="portrait__note">Selected to Rising Counsel 2020 - 2022</div>
    </div>
  </article>
  <article class="portrait" style="left:452px;top:345px;transform:rotate(-2deg)">
    <div class="portrait__photo" role="img" aria-label="Portrait photo of attorney Kendra Tolland"></div>
    <div class="portrait__caption">
      <div class="portrait__name">Kendra Tolland</div>
      <div class="portrait__note">Selected to Prime Counsel 2019 - 2022</div>
      <div class="portrait__note">Selected to Rising Counsel 2014 - 2018</div>
    </div>
  </article>
  <article class="portrait" style="left:664px;top:328px;transform:rotate(3deg)">
    <div class="portrait__photo" role="img" aria-label="Portrait photo of attorney Dana Whitcombe"></div>
    <div class="portrait__caption">
      <div class="portrait__name">Dana Whitcombe</div>
      <div class="portrait__note">Selected to Prime Counsel 2018 - 2022</div>
      <div class="portrait__note">Selected to Rising Counsel 2014 - 2017</div>
    </div>
  </article>

  <span class="pin" style="left:112px;top:250px;transform:rotate(-4deg)"></span>
  <span class="pin" style="left:330px;top:278px;transform:rotate(3deg)"></span>
  <span class="pin" style="left:548px;top:292px;transform:rotate(-2deg)"></span>
  <span class="pin" style="left:762px;top:268px;transform:rotate(5deg)"></span>

  <section class="tagline">
    <p class="tagline__lead">The Name is Hard to Remember.</p>
    <p class="tagline__close">The Results are Hard to Forget.</p>
  </section>

  <section class="practice">
    <h2 class="practice__title">Our practice areas</h2>
    <ul class="practice__list">
      <li>Business Litigation &amp; Dispute Resolution</li>
      <li>Entrepreneurship &amp; Small Business</li>
      <li>Contract and Commercial Law</li>
      <li>Employment &amp; Labor</li>
    </ul>
  </section>

  <footer class="contact">
    <div class="contact__row">
      <svg class="contact__icon" viewBox="0 0 24 24"><circle cx="12" cy="12" r="12" fill="var(--navy)"/><path d="M8.5 6.5l2 2-1.2 1.5a7 7 0 0 0 4.7 4.7l1.5-1.2 2 2-1.5 1.8C11 16.8 7.2 13 6.7 8z" fill="#fff"/></svg>
      <span>555-014-2290</span>
    </div>
    <div class="contact__row">
      <svg class="contact__icon" viewBox="0 0 24 24"><circle cx="12" cy="12" r="11" fill="none" stroke="var(--navy)" stroke-width="2"/><ellipse cx="12" cy="12" rx="4.5" ry="11" fill="none" stroke="var(--navy)" stroke-width="1.6"/><path d="M1 12h22M3 7h18M3 17h18" stroke="var(--navy)" stroke-width="1.4"/></svg>
      <span>www.mtplawgroup.example</span>
    </div>
  </footer>

  <div class="social" aria-label="Social media links">
    <span class="social__slot"></span><span class="social__slot"></span><span class="social__slot"></span><span class="social__slot"></span>
  </div>
</main>
</body>
</html>
```